Business card for a doctor's practice

Would like a business card for a Pulmonary ( lung) doctor. I would like to include a logo with something in reference to air or oxygen or lungs. Would like the color red included somehow. Name of the company is Breathwell Medical Associates of Eastern Ridgeford and we specialize in Pulmonary Medicine,. I would like something streamlined and modern
Target Market(s)
Patients, hospitals, other doctors
Industry/Entity Type
Business
Contact Information for Business Card
Would like business details superimposed on a logo somehow

```html
<!DOCTYPE html>
<html lang="en">
<head>
<meta charset="utf-8">
<title>Breathwell Medical Associates – Business Card</title>
<link rel="stylesheet" href="https://fonts.googleapis.com/css2?family=Arimo:wght@400;700&display=swap">
<style>
  :root {
    --backdrop: #2b2b2b;
    --card: #f4f4f4;
    --card-edge: #e2e2e2;
    --ink: #111111;
    --accent: #d7191f;
    --divider: #1a1a1a;
  }
  * { box-sizing: border-box; margin: 0; padding: 0; }
  html, body {
    width: 1200px;
    height: 997px;
    overflow: hidden;
    background: var(--backdrop);
    font-family: "Arimo", Arial, sans-serif;
  }
  .stage {
    width: 1200px;
    height: 997px;
    display: flex;
    align-items: center;
    justify-content: center;
  }
  .card {
    position: relative;
    width: 840px;
    height: 480px;
    border-radius: 28px;
    background: linear-gradient(160deg, #ffffff 0%, var(--card) 55%, var(--card-edge) 100%);
    display: grid;
    grid-template-columns: 1fr 1fr;
  }
  .brand {
    display: flex;
    align-items: center;
    justify-content: center;
    gap: 18px;
    padding: 0 40px 0 56px;
  }
  .brand-dot {
    flex: none;
    width: 26px;
    height: 26px;
    border-radius: 50%;
    background: var(--accent);
  }
  .brand-name {
    color: var(--accent);
    font-weight: 700;
    font-size: 27px;
    line-height: 1.2;
    text-transform: uppercase;
    letter-spacing: 0.5px;
  }
  .divider {
    position: absolute;
    left: 50%;
    top: 110px;
    width: 3px;
    height: 260px;
    transform: translateX(-50%);
    background: linear-gradient(to bottom, transparent 0%, var(--divider) 50%, transparent 100%);
  }
  .contact {
    padding: 118px 40px 0 56px;
  }
  .person-name {
    color: var(--ink);
    font-weight: 700;
    font-size: 28px;
  }
  .person-role {
    color: var(--accent);
    font-size: 22px;
    margin-top: 4px;
  }
  .details {
    list-style: none;
    margin-top: 34px;
  }
  .details li {
    display: flex;
    align-items: center;
    gap: 20px;
    color: var(--ink);
    font-size: 24px;
    margin-bottom: 18px;
  }
  .details svg {
    width: 22px;
    height: 22px;
    flex: none;
    fill: var(--accent);
  }
</style>
</head>
<body>
<main class="stage">
  <article class="card">
    <section class="brand">
      <span class="brand-dot"></span>
      <span class="brand-name">Breathwell Medical Associates of Eastern Ridgeford</span>
    </section>
    <span class="divider"></span>
    <section class="contact">
      <h1 class="person-name">Daniel Hartwell</h1>
      <p class="person-role">Chairman</p>
      <ul class="details">
        <li>
          <svg viewBox="0 0 24 24" aria-hidden="true"><path d="M3 8c0-2 3-4 9-4s9 2 9 4v2h-5V8.5c-1-.6-2.5-.9-4-.9s-3 .3-4 .9V10H3zM6 12h12l2 7H4z"/></svg>
          <span>0402718354</span>
        </li>
        <li>
          <svg viewBox="0 0 24 24" aria-hidden="true"><path d="M2 5h20v14H2zM4 7v.5l8 5.5 8-5.5V7z"/></svg>
          <span>info@bmaer.com</span>
        </li>
        <li>
          <svg viewBox="0 0 24 24" aria-hidden="true"><path d="M12 2a10 10 0 1 0 0 20 10 10 0 0 0 0-20zm0 2c1.2 1.4 2 3.5 2.2 6H9.8C10 7.5 10.8 5.4 12 4zM4.1 11h3.7c.1 2.3.7 4.4 1.7 6a8 8 0 0 1-5.4-6zm0-2a8 8 0 0 1 5.4-5c-1 1.6-1.6 3-1.7 5zm5.7 2h4.4c-.2 2.5-1 4.6-2.2 6-1.2-1.4-2-3.5-2.2-6zm6.4 0h3.7a8 8 0 0 1-5.4 6c1-1.6 1.6-3.7 1.7-6zm0-2c-.1-2-.7-3.4-1.7-5a8 8 0 0 1 5.4 5z"/></svg>
          <span>www.bmaer.com</span>
        </li>
      </ul>
    </section>
  </article>
</main>
</body>
</html>
```